Australian IT Company requires Business Card Design

Bluepeak is an Australian company that specialises in IT consulting & support, software development, project management, network services.

We have been in business for 15 years.

* We require a business card with the following on it:
Logo
Address
Contact Details
Space for staff name, title & mobile number

Industry/Entity Type

Software

```html
<!DOCTYPE html>
<html lang="en">
<head>
<meta charset="utf-8">
<title>Bluepeak Business Card</title>
<link href="https://fonts.googleapis.com/css2?family=Open+Sans:wght@400;600;700&display=swap" rel="stylesheet">
<style>
  :root {
    --brand-blue: #5f8fb4;
    --brand-blue-deep: #3f6e96;
    --ink-grey: #555a60;
    --soft-grey: #8a8f94;
    --paper: #ffffff;
    --backdrop: #ecebe8;
  }
  * { margin: 0; padding: 0; box-sizing: border-box; }
  html, body {
    width: 1200px; height: 800px; overflow: hidden;
    background: var(--backdrop);
    font-family: "Open Sans", Arial, sans-serif;
  }
  .stage { position: relative; width: 1200px; height: 800px; }

  .card { position: absolute; box-shadow: 0 6px 18px rgba(0,0,0,0.18); }

  /* Reverse side */
  .card-back {
    left: 90px; top: 110px; width: 354px; height: 580px;
    background: linear-gradient(160deg, var(--brand-blue) 0%, var(--brand-blue-deep) 100%);
    display: flex; flex-direction: column; align-items: center; justify-content: center; gap: 18px;
  }
  .card-back .brand-square { width: 54px; height: 54px; background: var(--paper); }
  .card-back .brand-name {
    color: var(--paper); font-weight: 700; font-size: 26px; letter-spacing: 2px;
  }

  /* Front side */
  .card-front {
    left: 500px; top: 223px; width: 600px; height: 366px;
    background: var(--paper);
  }
  .front-square {
    position: absolute; left: 40px; top: 44px; width: 150px; height: 150px;
    background: var(--brand-blue);
  }
  .wordmark {
    position: absolute; right: 36px; top: 34px; text-align: right;
  }
  .wordmark .brand-name {
    color: var(--brand-blue-deep); font-weight: 700; font-size: 50px; line-height: 1; letter-spacing: 1px;
  }
  .wordmark .tagline {
    margin-top: 6px; color: var(--ink-grey); font-size: 11.5px; letter-spacing: 5.4px; text-transform: uppercase;
  }

  .staff { position: absolute; left: 218px; top: 124px; }
  .staff-name { font-size: 19px; font-weight: 700; letter-spacing: 0.5px; color: var(--ink-grey); }
  .staff-name .first { color: var(--brand-blue); }
  .staff-title { font-size: 12px; color: var(--soft-grey); margin-top: -2px; }

  .contacts { position: absolute; left: 218px; top: 182px; list-style: none; }
  .contacts li {
    display: flex; align-items: center; gap: 8px;
    font-size: 14px; color: var(--ink-grey); line-height: 22px;
  }
  .contacts svg { width: 13px; height: 13px; flex: none; }

  .address {
    position: absolute; left: 218px; top: 266px;
    font-size: 14px; color: var(--soft-grey); text-transform: uppercase; line-height: 22px; font-style: normal;
  }
</style>
</head>
<body>
<div class="stage">
  <section class="card card-back" aria-label="Card reverse">
    <div class="brand-square"></div>
    <div class="brand-name">BLUEPEAK</div>
  </section>

  <section class="card card-front" aria-label="Card front">
    <div class="front-square"></div>
    <header class="wordmark">
      <div class="brand-name">BLUEPEAK</div>
      <div class="tagline">Technology you can trust</div>
    </header>

    <div class="staff">
      <div class="staff-name"><span class="first">DANIEL</span> MARSH</div>
      <div class="staff-title">Director</div>
    </div>

    <ul class="contacts">
      <li>
        <svg viewBox="0 0 13 13" aria-hidden="true"><rect width="13" height="13" rx="2" fill="#5f8fb4"/><rect x="4" y="2.5" width="5" height="8" rx="1" fill="none" stroke="#fff" stroke-width="1.2"/></svg>
        +61 3 9048 2275
      </li>
      <li>
        <svg viewBox="0 0 13 13" aria-hidden="true"><rect width="13" height="13" rx="2" fill="#5f8fb4"/><rect x="2.5" y="3.5" width="8" height="6" fill="none" stroke="#fff" stroke-width="1.1"/><path d="M2.5 3.5 L6.5 7 L10.5 3.5" fill="none" stroke="#fff" stroke-width="1.1"/></svg>
        daniel@bluepeak.net.au
      </li>
      <li>
        <svg viewBox="0 0 13 13" aria-hidden="true"><rect width="13" height="13" rx="2" fill="#5f8fb4"/><circle cx="6.5" cy="6.5" r="4" fill="none" stroke="#fff" stroke-width="1.1"/><path d="M2.5 6.5 H10.5 M6.5 2.5 C4.5 5 4.5 8 6.5 10.5 C8.5 8 8.5 5 6.5 2.5" fill="none" stroke="#fff" stroke-width="0.9"/></svg>
        www.bluepeak.net.au
      </li>
    </ul>

    <address class="address">
      14 Harbour Lane<br>
      Unit 5, Kingsbury VIC 3085
    </address>
  </section>
</div>
</body>
</html>
```